Book jacket for Drumlore

We need a book jacket design (hard cover front, back, spine, flaps; soft cover and eBook). for a social psychology book with the general cluelessness (being "out of it") of how people function both in their personal and social lives. This is the third book written by the author, a practicing psychiatrist, and the content centers on a single subject, people's lack of genuine emotional contact, their cluelessness with themselves and with current national and world events.

Target Market(s)

People who want to better understand the state the nation and world is in now, and what they can do about it.

Font styles to use
Serif
Sans Serif

Requirements
Must have
• Bold, eye-catching cover
Nice to have
• Like the idea of separating the title word (drum lore) to better emphasize the concept of lack of contact

```html
<!DOCTYPE html>
<html lang="en">
<head>
<meta charset="utf-8">
<title>Drumlore – Book Cover</title>
<link rel="stylesheet" href="https://fonts.googleapis.com/css2?family=Bebas+Neue&family=Lato:wght@400;700&display=swap">
<style>
  :root {
    --backdrop: #a9a9a9;
    --paper: #f4f4f4;
    --signal-red: #f0262b;
    --ink-grey: #4a4a4c;
    --caption-grey: #5c5c5e;
  }
  html, body {
    margin: 0;
    padding: 0;
    width: 1200px;
    height: 900px;
    overflow: hidden;
    background: var(--backdrop);
  }
  .stage {
    position: relative;
    width: 1200px;
    height: 900px;
  }
  .front-cover {
    position: absolute;
    left: 360px;
    top: 70px;
    width: 480px;
    height: 760px;
    background: var(--paper);
    box-shadow: 0 18px 40px rgba(0,0,0,0.18);
  }
  .front-cover svg { display: block; }
  .title-word {
    font-family: "Bebas Neue", "Arial Narrow", sans-serif;
    font-size: 168px;
    letter-spacing: -1px;
  }
  .title-word--upper { fill: var(--signal-red); }
  .title-word--lower { fill: var(--ink-grey); }
  .subtitle {
    font-family: "Lato", "Helvetica Neue", sans-serif;
    font-size: 15px;
    letter-spacing: 1px;
    fill: var(--caption-grey);
  }
  .author-name {
    font-family: "Lato", "Helvetica Neue", sans-serif;
    font-size: 27px;
    letter-spacing: 1px;
    fill: var(--ink-grey);
  }
  .arrow--left { fill: var(--signal-red); }
  .arrow--right { fill: var(--ink-grey); }
</style>
</head>
<body>
<main class="stage">
  <section class="front-cover" aria-label="Drumlore front cover">
    <svg width="480" height="760" viewBox="0 0 480 760" xmlns="http://www.w3.org/2000/svg">
      <g class="subtitle">
        <text x="60" y="150">THE</text>
        <text x="60" y="170">QUIET</text>
        <text x="60" y="190">LOSS OF</text>
        <text x="60" y="210">CONTACT</text>
      </g>

      <g class="arrow arrow--left">
        <rect x="62" y="244" width="268" height="12"/>
        <polygon points="66,234 66,266 40,250"/>
      </g>

      <text class="title-word title-word--upper" x="60" y="420">DRUM</text>
      <text class="title-word title-word--lower" x="180" y="570">LORE</text>

      <g class="arrow arrow--right">
        <rect x="180" y="604" width="240" height="12"/>
        <polygon points="416,594 416,626 442,610"/>
      </g>

      <g class="author-name">
        <text x="180" y="670">MARTIN</text>
        <text x="180" y="704">VELSOR M.D.</text>
      </g>
    </svg>
  </section>
</main>
</body>
</html>
```